Ablaufgrafik KlickWerkstatt
Zielgruppe
KlickWerkstatt: Content Marketing-Lösung für KMU
Ohne Aufwand verleiht KlickWerkstatt Inhalten (Produkt-Meldungen, Presse-Mitteilungen, Blog-Artikel, …) die notwendige Reichweite um Neukundenkontakte zu generieren.
Der Content geht über alle Kanäle: Web, Mail und Social.
Der KlickWerkstatt bietet flexible und maßgeschneiderte Online Marketing Lösungen, die sich am Bedarf hinsichtlich Quantität, Qualität, den Kunden-Bedürfnissen und dem Budget angleichen. Bis hin zu individuell selektierten Verteilern.
Aufgabenstellung
Es soll eine Ablaufgrafik erstellt werden, die visualisiert "Was passiert mit meinem Content über den KlickWerkstatt": Eine Prozess-Visualisierung.
Die Ablaufgrafik wird als JPG/PNG bei klickwerkstatt.de eingebunden: Mit klick öffnet sich eine bildschirmfüllende Grafik. Ebenso soll die Grafik im factsheet (pdf) eingebunden werden.
- CI gemäß www.klickwerkstatt.de
- Anschauung und Info: factsheet-PDF http://kurzlink-beispiel.de/Rw7TqZ
- Logo: http://kurzlink-beispiel.de/Jm3VbK
Skizze zum Aufbau und den Inhalten für die Ablaufgrafik: s. Dateianlage (pdf)

```html
<!DOCTYPE html>
<html lang="de">
<head>
<meta charset="utf-8">
<title>Ablaufgrafik KlickWerkstatt</title>
<link rel="stylesheet" href="https://fonts.googleapis.com/css2?family=Open+Sans:wght@400;600;700&display=swap">
<style>
  :root {
    --ink: #3d4450;
    --text: #4a4a4a;
    --line: #d5d5d5;
    --box-border: #dedede;
    --accent: #57c1df;
    --teal: #6cc5bd;
    --blue: #1aa7dd;
    --white: #ffffff;
  }
  * { margin: 0; padding: 0; box-sizing: border-box; }
  html, body { width: 1200px; height: 2342px; overflow: hidden; background: var(--white); }
  body { font-family: "Open Sans", Arial, sans-serif; color: var(--text); }
  .canvas { position: relative; width: 1200px; height: 2342px; overflow: hidden; }
  .decor, .connectors { position: absolute; left: 0; top: 0; }

  .brand { position: absolute; left: 102px; top: 72px; display: flex; align-items: center; gap: 14px; }
  .brand-mark { width: 34px; height: 34px; background: #f2a22b; }
  .brand-name { font-size: 38px; font-weight: 600; color: #3a3f47; letter-spacing: -0.5px; }

  .step { position: absolute; left: 0; width: 375px; height: 67px; display: flex; }
  .step-label { width: 295px; background: var(--ink); color: var(--white); font-size: 29px; display: flex; align-items: center; justify-content: center; letter-spacing: 0.5px; }
  .step-label b { font-weight: 700; margin-right: 8px; }
  .step-tab { flex: 1; background: var(--accent); }

  .highlight { position: absolute; height: 57px; background: linear-gradient(90deg, var(--teal), var(--blue)); color: var(--white); font-size: 27px; font-weight: 600; display: flex; align-items: center; justify-content: center; }

  .node { position: absolute; border: 2px solid var(--box-border); background: var(--white); font-size: 22px; line-height: 28px; text-align: center; display: flex; flex-direction: column; align-items: center; justify-content: center; color: var(--text); }
  .node .gap { height: 18px; }

  .channel { position: absolute; width: 164px; height: 164px; border-radius: 50%; background: var(--accent); color: var(--white); font-size: 28px; display: flex; flex-direction: column; align-items: center; justify-content: center; }
  .channel svg { margin-bottom: 6px; }

  .analytics { position: absolute; left: 514px; top: 1700px; width: 188px; height: 141px; border-radius: 6px; background: linear-gradient(135deg, #eef1f3, #dfe4e8 60%, #e98a5d); }

  .audience { position: absolute; left: 225px; top: 1917px; display: grid; grid-template-columns: repeat(9, 74px); gap: 9px 10.5px; }
  .person { width: 74px; height: 74px; border-radius: 50%; display: flex; align-items: center; justify-content: center; }

  .tagline { position: absolute; left: 372px; top: 2232px; width: 454px; height: 63px; border: 2px solid var(--box-border); font-size: 22px; font-weight: 600; color: var(--text); display: flex; align-items: center; justify-content: center; }
</style>
</head>
<body>
<div class="canvas">

  <svg class="decor" width="1200" height="700" aria-hidden="true">
    <defs>
      <linearGradient id="arcA" x1="0" y1="0" x2="1" y2="0">
        <stop offset="0" stop-color="#8ec9b6"/><stop offset="1" stop-color="#52c0e2"/>
      </linearGradient>
      <linearGradient id="arcB" x1="0" y1="0" x2="1" y2="1">
        <stop offset="0" stop-color="#9ccaa9"/><stop offset="1" stop-color="#4ec1e8"/>
      </linearGradient>
    </defs>
    <circle cx="886" cy="-118" r="291" fill="url(#arcA)" opacity="0.95"/>
    <circle cx="1200" cy="295" r="312" fill="url(#arcB)" opacity="0.9"/>
    <path d="M1015 40 L1200 470 L1200 0 L1120 0 Z" fill="#0a93b8" opacity="0.55"/>
  </svg>

  <div class="brand">
    <span class="brand-mark"></span>
    <span class="brand-name">KlickWerkstatt</span>
  </div>

  <svg class="connectors" width="1200" height="2342" fill="none" stroke="#d5d5d5" stroke-width="2" aria-hidden="true">
    <!-- Erstellen -->
    <path d="M600 355 V415 M439 415 H758 M439 415 V477 M758 415 V477"/>
    <path d="M421 459 L439 477 L457 459 M740 459 L758 477 L776 459"/>
    <path d="M439 534 V600 M758 534 V600"/>
    <path d="M421 582 L439 600 L457 582 M740 582 L758 600 L776 582"/>
    <path d="M439 658 V721 H758 V658 M600 721 V778"/>
    <path d="M582 760 L600 778 L618 760"/>
    <!-- Verbreiten -->
    <path d="M600 838 V895 M285 895 H918 M285 895 V942 M600 895 V942 M918 895 V942"/>
    <path d="M267 924 L285 942 L303 924 M582 924 L600 942 L618 924 M900 924 L918 942 L936 924"/>
    <path d="M285 1114 V1172 M600 1114 V1172 M918 1114 V1172"/>
    <path d="M267 1154 L285 1172 L303 1154 M582 1154 L600 1172 L618 1154 M900 1154 L918 1172 L936 1154"/>
    <path d="M285 1274 V1291 M600 1355 V1372 M600 1435 V1454 M918 1243 V1261 M918 1324 V1342"/>
    <path d="M285 1355 V1561 H918 V1405 M600 1517 V1688"/>
    <!-- Auswerten -->
    <path d="M582 1670 L600 1688 L618 1670"/>
    <path d="M600 1841 V1907 M582 1889 L600 1907 L618 1889"/>
    <path d="M600 2078 V2130 M582 2112 L600 2130 L618 2112"/>
  </svg>

  <div class="step" style="top:292px"><div class="step-label"><b>1.</b>ERSTELLEN</div><div class="step-tab"></div></div>
  <div class="step" style="top:777px"><div class="step-label"><b>2.</b>VERBREITEN</div><div class="step-tab"></div></div>
  <div class="step" style="top:1611px"><div class="step-label"><b>3.</b>AUSWERTEN</div><div class="step-tab"></div></div>

  <div class="highlight" style="left:488px; top:297px; width:219px;">Ihre News</div>

  <div class="node" style="left:323px; top:477px; width:177px; height:57px;">Mail</div>
  <div class="node" style="left:695px; top:477px; width:178px; height:57px;">Login</div>
  <div class="node" style="left:256px; top:602px; width:244px; height:56px;">Einstellerservice</div>
  <div class="node" style="left:695px; top:602px; width:264px; height:56px;">Redaktionssystem</div>

  <div class="highlight" style="left:482px; top:781px; width:233px;">Ihr Newsroom</div>

  <div class="channel" style="left:201px; top:950px;">
    <svg width="40" height="44" viewBox="0 0 40 44"><path d="M4 4 L36 18 L22 22 L30 38 L24 41 L16 25 L6 34 Z" fill="#ffffff" stroke="#e36b3f" stroke-width="2.5" stroke-linejoin="round"/></svg>
    Web
  </div>
  <div class="channel" style="left:518px; top:950px;">
    <svg width="50" height="44" viewBox="0 0 50 44"><rect x="12" y="2" width="26" height="24" fill="#ffffff"/><path d="M17 9 H33 M17 14 H33 M17 19 H28" stroke="#e36b3f" stroke-width="2"/><path d="M2 18 L25 34 L48 18 V42 H2 Z" fill="#3f9fb8"/></svg>
    Mail
  </div>
  <div class="channel" style="left:835px; top:950px;">
    <svg width="58" height="44" viewBox="0 0 58 44"><rect x="20" y="10" width="36" height="24" rx="3" fill="#3d4450"/><path d="M44 34 L50 42 L50 34 Z" fill="#3d4450"/><rect x="2" y="2" width="40" height="26" rx="3" fill="#ffffff"/><path d="M8 28 L8 36 L16 28 Z" fill="#ffffff"/><path d="M8 10 H36 M8 15 H36 M8 20 H28" stroke="#57c1df" stroke-width="2"/></svg>
    Social
  </div>

  <div class="node" style="left:144px; top:1179px; width:270px; height:95px;">Portale<br>im Medien-Netzwerk</div>
  <div class="node" style="left:144px; top:1291px; width:270px; height:64px;">Suchwerk &amp; Co.</div>

  <div class="node" style="left:465px; top:1179px; width:270px; height:176px;">Marketing-Verteiler<span class="gap"></span>Fach-/führungskräfte,<br>Entscheider,<br>Meinungsmacher, …</div>
  <div class="node" style="left:465px; top:1372px; width:270px; height:63px;">Journalisten-Verteiler</div>
  <div class="node" style="left:465px; top:1454px; width:270px; height:63px;">Individuelle-Verteiler</div>

  <div class="node" style="left:785px; top:1179px; width:270px; height:64px;">Freundesnetz</div>
  <div class="node" style="left:785px; top:1261px; width:270px; height:63px;">Kurzfunk</div>
  <div class="node" style="left:785px; top:1342px; width:270px; height:63px;">Berufsnetz</div>

  <div class="analytics" role="img" aria-label="Laptop mit Auswertungs-Dashboard und Lupe"></div>

  <div class="audience" aria-label="Erreichte Zielgruppe">
    <svg width="0" height="0" style="position:absolute"><defs><symbol id="user" viewBox="0 0 40 40"><circle cx="20" cy="13" r="8" fill="none" stroke="#ffffff" stroke-width="2"/><path d="M5 36 C6 26 13 23 20 23 C27 23 34 26 35 36 Z" fill="none" stroke="#ffffff" stroke-width="2" stroke-linejoin="round"/></symbol></defs></svg>
    <div class="person" style="background:#63c0b8"><svg width="40" height="40"><use href="#user"/></svg></div>
    <div class="person" style="background:#5abdbf"><svg width="40" height="40"><use href="#user"/></svg></div>
    <div class="person" style="background:#50bbc6"><svg width="40" height="40"><use href="#user"/></svg></div>
    <div class="person" style="background:#46b8cc"><svg width="40" height="40"><use href="#user"/></svg></div>
    <div class="person" style="background:#3cb5d1"><svg width="40" height="40"><use href="#user"/></svg></div>
    <div class="person" style="background:#33b2d5"><svg width="40" height="40"><use href="#user"/></svg></div>
    <div class="person" style="background:#29afd9"><svg width="40" height="40"><use href="#user"/></svg></div>
    <div class="person" style="background:#20acdc"><svg width="40" height="40"><use href="#user"/></svg></div>
    <div class="person" style="background:#1aa9de"><svg width="40" height="40"><use href="#user"/></svg></div>
    <div class="person" style="background:#63c0b8"><svg width="40" height="40"><use href="#user"/></svg></div>
    <div class="person" style="background:#5abdbf"><svg width="40" height="40"><use href="#user"/></svg></div>
    <div class="person" style="background:#50bbc6"><svg width="40" height="40"><use href="#user"/></svg></div>
    <div class="person" style="background:#46b8cc"><svg width="40" height="40"><use href="#user"/></svg></div>
    <div class="person" style="background:#3cb5d1"><svg width="40" height="40"><use href="#user"/></svg></div>
    <div class="person" style="background:#33b2d5"><svg width="40" height="40"><use href="#user"/></svg></div>
    <div class="person" style="background:#29afd9"><svg width="40" height="40"><use href="#user"/></svg></div>
    <div class="person" style="background:#20acdc"><svg width="40" height="40"><use href="#user"/></svg></div>
    <div class="person" style="background:#1aa9de"><svg width="40" height="40"><use href="#user"/></svg></div>
  </div>

  <div class="highlight" style="left:482px; top:2134px; width:233px;">Ihre Firma</div>

  <div class="tagline">Einfach. Erfolgreich. Kunden gewinnen.</div>
</div>
</body>
</html>
```